Vorlisk.com Redesign

Please read the notes and see the site-map attached.
Updates

We are looking for something highly creative. Please provide your best work. Best of luck and thank you very much for your hard work!

Project Deadline Extended
Reason: I am seeing good designs but I am not seeing great designs. I really need a design that is unique and is going to wow me. No one is required to stick to the existing color schemes etc. You are free to use other colors etc. I am seeing a lot of the same colors that are used on the site now.

Target Market(s)

Business and entrepreneurs mainly. People looking to build applications, software or launch web or mobile tech products.

Colors

Designer to choose colors to be used in the design.

Requirements
Must have
• See my attached html file.
Nice to have
Should not have
• No sure

```html
<!DOCTYPE html>
<html lang="en">
<head>
<meta charset="utf-8">
<title>Vorlisk — Web &amp; Mobile Products</title>
<link rel="stylesheet" href="https://fonts.googleapis.com/css2?family=Lato:ital,wght@0,300;0,400;0,700;1,400&display=swap">
<style>
:root{
  --green:#6fb33a;
  --green-light:#a4d65e;
  --green-dark:#4d8f22;
  --ink:#333;
  --muted:#777;
  --hero-bg:#f4f4f4;
  --line:#e4e4e4;
  --footer:#333333;
  --footer-bottom:#2a2a2a;
  --footer-text:#9a9a9a;
}
*{margin:0;padding:0;box-sizing:border-box}
html,body{width:939px;height:1200px;overflow:hidden}
body{font-family:'Lato',sans-serif;color:var(--ink);background:#fff;position:relative}

.site-header{position:absolute;left:0;top:0;width:939px;height:58px;background:#fff;border-bottom:1px solid #e2e2e2}
.brand{position:absolute;left:152px;top:10px;display:flex;align-items:center;gap:8px;font-size:27px;font-weight:700;color:var(--green);letter-spacing:-.5px}
.brand-mark{width:26px;height:26px;border-radius:50%;background:#2d4d5c}
.main-nav{position:absolute;left:413px;top:24px;font-size:10.5px;color:#444}
.main-nav a{color:#444;text-decoration:none;position:absolute;white-space:nowrap}
.main-nav .active::before{content:"";position:absolute;left:0;right:0;top:-24px;height:2px;background:var(--green)}
.client-login{position:absolute;left:715px;top:18px;width:70px;height:24px;background:var(--green);color:#fff;font-size:10px;line-height:24px;text-align:center;border-radius:2px}

.hero{position:absolute;left:0;top:58px;width:939px;height:291px;background:var(--hero-bg);border-bottom:1px solid #e0e0e0}
.hero-title{position:absolute;left:154px;top:80px;font-size:19px;font-weight:300;color:var(--green);line-height:23px;letter-spacing:.4px}
.hero-sub{position:absolute;left:154px;top:131px;font-size:17px;font-weight:300;color:#2d4d5c;line-height:22px;letter-spacing:.4px}
.hire-btn{position:absolute;left:154px;top:187px;width:137px;height:31px;background:linear-gradient(#b7df7b,#98cc55);border:1px solid #8cbf4c;font-size:8px;font-weight:700;color:#3e6b1a;display:flex;align-items:center}
.hire-btn .tick{width:27px;height:100%;border-right:1px solid #8cbf4c;display:flex;align-items:center;justify-content:center}
.hire-btn span{padding-left:12px}
.video{position:absolute;left:410px;top:42px;width:374px;height:208px;background:#000;box-shadow:0 16px 18px -10px rgba(0,0,0,.35)}
.video-art{position:absolute;inset:0;background:radial-gradient(circle at 50% 55%,#3f7a1c 0%,#1a3a0b 35%,#000 70%)}
.video-title{position:absolute;left:43px;top:8px;background:rgba(0,0,0,.7);padding:3px 6px}
.video-title b{display:block;font-size:10px;color:var(--green);font-weight:700}
.video-title small{font-size:6px;color:var(--green-dark)}
.video-controls{position:absolute;left:6px;bottom:6px;right:10px;height:26px;display:flex;align-items:center;gap:8px}
.play{width:44px;height:26px;background:rgba(40,40,40,.9);display:flex;align-items:center;justify-content:center}
.track{flex:1;height:10px;border:1px solid #666;position:relative}
.track i{position:absolute;left:1px;top:1px;bottom:1px;width:25%;background:var(--green)}
.track em{position:absolute;left:25%;top:1px;bottom:1px;width:10%;background:#555}
.hd{font-size:6px;color:#ddd;border:1px solid #ddd;padding:0 2px}
.slide-arrow{position:absolute;top:112px;width:42px;height:42px;background:#8a8a8a;display:flex;align-items:center;justify-content:center}

.service{position:absolute;top:392px;width:202px}
.service-img{height:106px;width:202px}
.service h3{font-size:11.5px;font-weight:400;color:#333;margin-top:17px}
.service p{font-size:8px;line-height:13.5px;color:var(--muted);margin-top:7px}

.section-title{position:absolute;font-size:11.5px;font-weight:400;color:#333;display:flex;align-items:center}
.section-title::after{content:"";display:block;height:3px;border-top:1px solid var(--line);border-bottom:1px solid var(--line);margin-left:12px;flex:1}
.quote{position:absolute;left:158px;top:674px;width:303px;height:100px;background:#f4f2f2;padding:14px 16px;font-size:7.4px;line-height:13.5px;font-style:italic;color:#666}
.quote::after{content:"";position:absolute;left:26px;bottom:-10px;border-right:12px solid transparent;border-top:10px solid #f4f2f2}
.quote-author{position:absolute;left:158px;top:782px;font-size:8px;color:#444;display:flex;align-items:center;gap:10px}
.avatar{width:16px;height:18px;background:#5a4a5c;border-radius:3px}
.who-list{position:absolute;left:486px;top:663px;list-style:none}
.who-list li{display:flex;align-items:center;gap:10px;height:23px;font-size:8px;color:#555}
.who-list .dot{width:12px;height:12px;border-radius:50%;background:var(--green);display:flex;align-items:center;justify-content:center}

.clients{position:absolute;top:920px;left:154px;width:632px;display:flex;justify-content:space-between;align-items:center}
.client{font-size:15px;font-weight:700;color:#555;display:flex;align-items:center;gap:6px}
.client .sq{width:10px;height:10px;background:#555}

.site-footer{position:absolute;left:0;top:1002px;width:939px;height:198px;background:var(--footer);border-top:4px solid #e6e6e6}
.footer-brand{position:absolute;left:158px;top:34px;display:flex;flex-direction:column;align-items:center;gap:8px;width:108px}
.footer-brand .brand-mark{width:28px;height:28px;background:#2f5a6c}
.footer-brand b{font-size:18px;color:var(--green);font-weight:700}
.footer-col{position:absolute;top:35px;font-size:8px;line-height:14.7px;color:var(--footer-text)}
.footer-col h4{font-size:8.5px;color:#fff;font-weight:400;letter-spacing:.4px;margin-bottom:10px}
.footer-col a{color:var(--green);text-decoration:none}
.footer-col .time{font-size:6.5px;color:#666}
.footer-bottom{position:absolute;left:0;top:156px;width:939px;height:38px;background:var(--footer-bottom);font-size:7.5px;color:#999;padding:14px 0 0 154px}
.online{position:absolute;left:664px;top:174px;width:128px;height:20px;background:var(--green);color:#fff;font-size:9px;font-weight:700;display:flex;align-items:center;gap:10px;padding-left:8px;border-radius:3px 3px 0 0}
</style>
</head>
<body>

<header class="site-header">
  <div class="brand"><span class="brand-mark"></span>vorlisk</div>
  <nav class="main-nav">
    <a class="active" style="left:0">Who we are</a>
    <a style="left:74px">What we do</a>
    <a style="left:143px">Our Work</a>
    <a style="left:207px">Reach us</a>
    <a style="left:265px">Blog</a>
  </nav>
  <div class="client-login">Client Login</div>
</header>

<section class="hero">
  <div class="slide-arrow" style="left:0">
    <svg width="10" height="14" viewBox="0 0 10 14"><path d="M8 1 2 7l6 6" fill="none" stroke="#fff" stroke-width="2"/></svg>
  </div>
  <div class="slide-arrow" style="left:897px">
    <svg width="10" height="14" viewBox="0 0 10 14"><path d="M2 1l6 6-6 6" fill="none" stroke="#fff" stroke-width="2"/></svg>
  </div>
  <h1 class="hero-title">We Create Web &amp; Mobile<br>Products That Delight Users</h1>
  <h2 class="hero-sub">Create Smiles and Deliver<br>More Than Expected</h2>
  <div class="hire-btn">
    <div class="tick"><svg width="13" height="13" viewBox="0 0 13 13"><circle cx="6.5" cy="6.5" r="6.5" fill="#5e9e2c"/><path d="M3.5 6.8l2 2 4-4" fill="none" stroke="#cfeeaa" stroke-width="1.6"/></svg></div>
    <span>HIRE US NOW</span>
  </div>
  <div class="video">
    <div class="video-art" role="img" aria-label="Green illustrated mascot surrounded by tech icons on a dark background"></div>
    <div class="video-title"><b>Video Title Goes Here</b><small>from Dolores Amets</small></div>
    <div class="video-controls">
      <div class="play"><svg width="10" height="12" viewBox="0 0 10 12"><path d="M0 0l10 6-10 6z" fill="#fff"/></svg></div>
      <div class="track"><i></i><em></em></div>
      <span class="hd">HD</span>
      <svg width="8" height="8" viewBox="0 0 8 8"><path d="M1 1l6 6M7 1 1 7" stroke="#ddd" stroke-width="1.4"/></svg>
    </div>
  </div>
</section>

<article class="service" style="left:154px">
  <div class="service-img" role="img" aria-label="Close-up photo of HTML tags printed on paper" style="background:linear-gradient(135deg,#e8e8e8,#bdbdbd)"></div>
  <h3>Web Development</h3>
  <p>Lid est laborum dolo rumes fugats untras. Etharums ser quidem rerum facilis dolores nemis omnis fugats vitaes nemo minima rerums unsers sadips amets.</p>
</article>
<article class="service" style="left:369px">
  <div class="service-img" role="img" aria-label="Smartphone with colourful app icons bursting out" style="background:linear-gradient(135deg,#efefef,#c9d8e6)"></div>
  <h3>Mobile App Development</h3>
  <p>Lid est laborum dolo rumes fugats untras. Etharums ser quidem rerum facilis dolores nemis omnis fugats vitaes nemo minima rerums unsers sadips amets.</p>
</article>
<article class="service" style="left:584px">
  <div class="service-img" role="img" aria-label="Collage of software platform and framework marks" style="background:linear-gradient(135deg,#f0f0f0,#6aa3c4)"></div>
  <h3>Custom Software Development</h3>
  <p>Lid est laborum dolo rumes fugats untras. Etharums ser quidem rerum facilis dolores nemis omnis fugats vitaes nemo minima rerums unsers sadips amets.</p>
</article>

<h3 class="section-title" style="left:154px;top:636px;width:307px">What Client’s Say</h3>
<blockquote class="quote">“Neque porro quisquam est, qui dolorem ipsum quia dolor sit amet, consec tetur, adipisci velit, sed quia non numquam eius modi tempora incidunt utis labore et dolore magnam aliquam quaerat voluptatem. Ut enim ad minimas veniam, quis nostrum exercitationem ullam corporis suscipit laboriosam, nisi ut aliquid ex ea commodi consequatur slores amet untras vel illum qui.”</blockquote>
<div class="quote-author"><span class="avatar"></span><span><b>Jon Doe,</b> Company Inc.</span></div>

<h3 class="section-title" style="left:486px;top:636px;width:300px">Who We Are</h3>
<ul class="who-list">
  <li><span class="dot"><svg width="6" height="6" viewBox="0 0 6 6"><path d="M2 1l2 2-2 2" fill="none" stroke="#fff" stroke-width="1.2"/></svg></span>Cras rutrum leo at odio volutpat id blandit fugiats ipsum ornare.</li>
  <li><span class="dot"><svg width="6" height="6" viewBox="0 0 6 6"><path d="M2 1l2 2-2 2" fill="none" stroke="#fff" stroke-width="1.2"/></svg></span>Donec fermentum porttitor nunc, sit amet gravida est porttitor vel.</li>
  <li><span class="dot"><svg width="6" height="6" viewBox="0 0 6 6"><path d="M2 1l2 2-2 2" fill="none" stroke="#fff" stroke-width="1.2"/></svg></span>Maecenas quis nisi in uctus adipiscing sed vehicula tellus amet dolore.</li>
  <li><span class="dot"><svg width="6" height="6" viewBox="0 0 6 6"><path d="M2 1l2 2-2 2" fill="none" stroke="#fff" stroke-width="1.2"/></svg></span>Aenean faucibus sapien a odio varius aliquet voluptas sadips..</li>
  <li><span class="dot"><svg width="6" height="6" viewBox="0 0 6 6"><path d="M2 1l2 2-2 2" fill="none" stroke="#fff" stroke-width="1.2"/></svg></span>Suspendisse venenatis euismod ve vestibulum volutpat nibh imperdiets.</li>
</ul>

<h3 class="section-title" style="left:154px;top:862px;width:632px">Our Happy Clients</h3>
<div class="clients">
  <span class="client">Kestrel</span>
  <span class="client"><span class="sq"></span>Orbica</span>
  <span class="client">Plumline</span>
  <span class="client">Fernwick</span>
  <span class="client">Vidora</span>
  <span class="client">Maplecrate</span>
</div>

<footer class="site-footer">
  <div class="footer-brand"><span class="brand-mark"></span><b>vorlisk</b></div>
  <div class="footer-col" style="left:326px">
    <h4>PAGES</h4>
    Homepage<br>About Us<br>Works<br>Services<br>Contact
  </div>
  <div class="footer-col" style="left:452px">
    <h4>CONTACT</h4>
    Call us at (55) 014-2276<br>
    Email us at <a>hello@vorlisk.com</a><br>
    Follow <a>@Vorlisk</a> on Chirply<br>
    Have a look at our <a>Pixtrove stream</a>
  </div>
  <div class="footer-col" style="left:645px;width:150px">
    <h4>LATEST CHIRP</h4>
    Our latest work, pretty cute huh! And welcome all your comments, thanks guys.<br>
    <span class="time">About 5 hours ago</span>
  </div>
  <div class="footer-bottom">Copyright 2014 Vorlisk | &nbsp;All Rights Reserved</div>
  <div class="online">
    <svg width="12" height="10" viewBox="0 0 12 10"><path d="M1 1h10v6H5l-3 3V7H1z" fill="#fff"/></svg>
    We're Online!
  </div>
</footer>

</body>
</html>
```